Software Product Flyer Design

A established czech software company needs a marketing flyer to promote their software product and its modules.
The overall feel of the flyer must to be serious, but also eye-catching, enticing, clever and bold to attract customers.
Unifying graphic element is the new product logo.
The flyer would be A4, colour both sides and folded once (to give 4 pages of A5).
Title page - product logo with module name and module icon, short presentation of the product and list of its key features.
Inside pages - detailed informations with screenshots or graphical schemas.
Back side - informations about technical requirements and user support, contacts (address, phone, fax, e-mail, web pages - no social networks).
Product logo, module icon and some images attached.
Updates
Hello,
Reason: For organizational reasons we extending the deadline by 10 days.
FYI: We have uploaded the new ZIP file with previous version of our flyer.
Attached PDF file with text for inner pages.
Target Market(s)
Existing or new customers like municipalities, public authorities and nonprofit organizations.
Industry/Entity Type
Marketing
Requirements
Must have
- Winning designer must provide a template for Adobe InDesign based on his graphic design.
Avoid to using exotic fonts - in Czech we use Latin Extended characters (like áéěíýůčřžšťďň).
Nice to have
- Using graphic motif from product logo like as attached splash screen.

```html
<!DOCTYPE html>
<html lang="en">
<head>
<meta charset="utf-8">
<title>Velto Software Flyer</title>
<link rel="stylesheet" href="https://fonts.googleapis.com/css2?family=Arimo:wght@400;700&display=swap">
<style>
  :root {
    --ink: #000000;
    --paper: #ffffff;
    --accent-red: #e31e24;
    --photo-light: #e4ecef;
    --photo-mid: #b9c7cf;
    --photo-dark: #7f8f99;
  }
  html, body {
    margin: 0;
    padding: 0;
    width: 1200px;
    height: 848px;
    overflow: hidden;
    background: var(--ink);
  }
  .flyer {
    position: relative;
    width: 1200px;
    height: 848px;
    background: var(--ink);
    color: var(--paper);
    font-family: "Arimo", Arial, sans-serif;
    overflow: hidden;
  }
  .panel { position: absolute; top: 0; height: 848px; }
  .panel--back { left: 0; width: 597px; }
  .panel--cover { left: 597px; width: 603px; }

  /* Feature icons */
  .features {
    position: absolute;
    top: 100px;
    left: 28px;
    width: 532px;
    display: flex;
    justify-content: space-between;
  }
  .feature {
    width: 160px;
    text-align: center;
  }
  .feature__icon {
    display: block;
    width: 96px;
    height: 92px;
    margin: 0 auto 12px;
  }
  .feature__label {
    margin: 0;
    font-weight: 700;
    font-size: 13.5px;
    line-height: 16px;
    text-transform: uppercase;
  }

  /* Body copy */
  .copy {
    position: absolute;
    left: 48px;
    width: 502px;
    text-align: center;
  }
  .copy--first { top: 288px; }
  .copy--second { top: 410px; }
  .copy__heading {
    margin: 0;
    color: var(--accent-red);
    font-weight: 700;
    font-size: 20px;
    line-height: 24px;
  }
  .copy__text {
    margin: 0;
    font-size: 10.4px;
    line-height: 12.8px;
    text-align: justify;
    text-align-last: center;
  }

  /* Brand name */
  .brand {
    position: absolute;
    margin: 0;
    transform: translateX(-50%);
    font-weight: 700;
    font-size: 86px;
    line-height: 1;
    letter-spacing: -1px;
    color: var(--paper);
    white-space: nowrap;
  }
  .brand--back { left: 294px; top: 606px; }
  .brand--cover { left: 289px; top: 505px; }

  /* Contact */
  .contact {
    position: absolute;
    top: 748px;
    left: 0;
    width: 597px;
    margin: 0;
    text-align: center;
    font-style: normal;
    font-size: 15.6px;
    line-height: 20px;
  }

  /* Cover photo and band */
  .cover-visual {
    position: absolute;
    top: 0;
    left: 0;
    width: 603px;
    height: 470px;
  }

  .tagline {
    position: absolute;
    top: 638px;
    left: 0;
    width: 572px;
    margin: 0;
    text-align: center;
    font-size: 31px;
    line-height: 43px;
  }
  .tagline__lead { font-weight: 700; display: block; }
</style>
</head>
<body>
<main class="flyer">

  <section class="panel panel--back">
    <div class="features">
      <div class="feature">
        <svg class="feature__icon" viewBox="0 0 96 92" aria-hidden="true">
          <circle cx="52" cy="50" r="34" fill="var(--paper)"/>
          <path d="M32 56 A22 22 0 0 1 72 56" fill="none" stroke="var(--accent-red)" stroke-width="4"/>
          <line x1="52" y1="56" x2="66" y2="40" stroke="var(--accent-red)" stroke-width="4" stroke-linecap="round"/>
          <circle cx="52" cy="56" r="5" fill="var(--accent-red)"/>
        </svg>
        <p class="feature__label">Lorem ipsum<br>dolor sit amet</p>
      </div>
      <div class="feature">
        <svg class="feature__icon" viewBox="0 0 96 92" aria-hidden="true">
          <ellipse cx="48" cy="56" rx="34" ry="24" fill="var(--paper)"/>
          <rect x="28" y="70" width="10" height="18" rx="2" fill="var(--paper)"/>
          <rect x="58" y="70" width="10" height="18" rx="2" fill="var(--paper)"/>
          <rect x="78" y="48" width="10" height="12" rx="3" fill="var(--paper)"/>
          <circle cx="48" cy="14" r="11" fill="var(--accent-red)"/>
          <rect x="40" y="31" width="16" height="4" rx="2" fill="var(--ink)"/>
        </svg>
        <p class="feature__label">Lorem ipsum<br>dolor sit amet</p>
      </div>
      <div class="feature">
        <svg class="feature__icon" viewBox="0 0 96 92" aria-hidden="true">
          <path d="M6 50 L22 34 L38 50 L78 6 L94 22 L38 86 Z" fill="var(--paper)"/>
        </svg>
        <p class="feature__label">Lorem ipsum<br>dolor sit amet</p>
      </div>
    </div>

    <article class="copy copy--first">
      <h2 class="copy__heading">Lorem ipsum dolor sit amet</h2>
      <p class="copy__text">Lorem ipsum dolor sit amet, consectetur adipiscing elit. Nam eu urna eget massa tristique placerat. Nulla vestibulum feugiat vestibulum. Suspendisse potenti. Nam vel tortor mi. Duis sed felis id quam tristique porta et ac nulla. Sed convallis volutpat viverra. Fusce mattis lacus posuere sapien suscipit nec congue risus sagittis. Nam ut sem eget eros lobortis ornare eu id felis. Etiam enim nisl, tincidunt vitae mattis non, mollis sed neque.</p>
    </article>

    <article class="copy copy--second">
      <h2 class="copy__heading">Lorem ipsum dolor sit amet</h2>
      <p class="copy__text">consectetur adipiscing elit. Nam eu urna eget massa tristique placerat. Nulla vestibulum feugiat vestibulum. Suspendisse potenti. Nam vel tortor mi. Duis sed felis id quam tristique porta et ac nulla. Sed convallis volutpat viverra. Fusce mattis lacus posuere sapien suscipit nec congue risus sagittis. Nam ut sem eget eros lobortis ornare eu id felis. Etiam enim nisl, tincidunt vitae mattis non, mollis sed neque.</p>
    </article>

    <p class="brand brand--back">velto</p>

    <address class="contact">
      48 Harbor Lane. Portland, OR, 97201. USA<br>
      (555) 014-2290<br>
      hello@veltosoft.com
    </address>
  </section>

  <section class="panel panel--cover">
    <svg class="cover-visual" viewBox="0 0 603 470">
      <defs>
        <linearGradient id="photoTone" x1="0" y1="0" x2="1" y2="1">
          <stop offset="0" stop-color="var(--photo-mid)"/>
          <stop offset="0.55" stop-color="var(--photo-light)"/>
          <stop offset="1" stop-color="var(--photo-dark)"/>
        </linearGradient>
      </defs>
      <path d="M0 0 H603 V414 L0 446 Z" fill="url(#photoTone)" role="img" aria-label="Photo of a smiling businessman holding a mobile phone beside a laptop showing the software"/>
      <path d="M0 446 L603 414 L603 430 L0 462 Z" fill="var(--accent-red)"/>
    </svg>

    <p class="brand brand--cover">velto</p>

    <p class="tagline">
      <span class="tagline__lead">Lorem ipsum dolor</span>
      sit amet, consectetur<br>adipiscing elit.
    </p>
  </section>

</main>
</body>
</html>
```